Pizza Box cover art/design

13inch pizza box for Woodfired Pizza restaurant. Check out www.lumbrisk.com.au. Would prefer colours on box to be similar or complement lumbrisk logo. Would prefer Lumbrisk logo included but not essential, must include phone number, shop address, Instagram/Facebook address etc.
Target Market(s)
20-60 year olds
Colors
Designer to choose colors to be used in the design.
Requirements
Must have
- 13inch pizza box for Woodfired Pizza restaurant. Check out www.lumbrisk.com.au. Would prefer colours on box to be similar or complement lumbrisk logo. Would prefer Lumbrisk logo included but not essential, must include phone number, shop address, Instagram/Facebook address etc.
Nice to have
- Don't want the classic cartoon Italian pizza chef on box. Want more of a "cooler" modern design. We have live music playing some nights. We outdoor seating area that overlooks a lake. Check out our website www.lumbrisk.com.au to see more pics.

```html
<!DOCTYPE html>
<html lang="en">
<head>
<meta charset="utf-8">
<title>Lumbrisk Woodfired Pizza – 13 inch Box Sheet</title>
<link rel="stylesheet" href="https://fonts.googleapis.com/css2?family=Courgette&display=swap">
<style>
  :root {
    --maroon: #632326;
    --maroon-soft: #6e2d2f;
    --beige: #c9c19c;
    --cream: #ddd4ae;
    --rust: #9c4a24;
    --paper: #ffffff;
  }
  html, body {
    margin: 0;
    width: 1200px;
    height: 1200px;
    overflow: hidden;
    background: var(--paper);
  }
  .box-sheet {
    position: absolute;
    left: 0;
    top: 150px;
    width: 1200px;
    height: 900px;
    display: block;
  }
  .script { font-family: 'Courgette', cursive; }
  .flap { fill: var(--rust); }
  .panel-beige { fill: var(--beige); }
  .panel-maroon { fill: var(--maroon); }
  .tuck { fill: var(--beige); }
  .strip-text { fill: var(--maroon); font-size: 17px; }
  .brand-dark { fill: var(--maroon); font-size: 26px; letter-spacing: 3px; }
  .brand-light { fill: var(--cream); font-size: 30px; letter-spacing: 3px; }
  .brand-square-rust { fill: var(--rust); }
  .lid-text { fill: var(--cream); }
  .lid-rule { stroke: var(--rust); stroke-width: 2; }
  .address { font-size: 10.5px; }
  .headline { font-size: 24px; }
  .connect-title { font-size: 11px; }
  .connect-item { font-size: 9px; }
  .order-label { font-size: 19px; }
  .order-phone { font-size: 21px; }
  .social-dot { fill: var(--rust); }
  .phone-icon { fill: var(--maroon); }
  .phone-text { fill: var(--maroon); font-size: 18px; }
</style>
</head>
<body>
<svg class="box-sheet" viewBox="40 20 880 660" xmlns="http://www.w3.org/2000/svg" aria-label="Lumbrisk 13 inch pizza box sheet">

  <!-- corner flaps -->
  <rect class="flap" x="56" y="32" width="91" height="158"/>
  <rect class="flap" x="56" y="505" width="91" height="157"/>
  <rect class="flap" x="462" y="32" width="90" height="158"/>
  <rect class="flap" x="462" y="505" width="90" height="157"/>

  <!-- side strips -->
  <rect class="panel-beige" x="147" y="145" width="315" height="45"/>
  <rect class="panel-beige" x="552" y="145" width="316" height="45"/>
  <rect class="panel-beige" x="147" y="505" width="315" height="45"/>
  <rect class="panel-beige" x="552" y="505" width="316" height="45"/>

  <text class="script strip-text" x="300" y="173" text-anchor="middle">Lumbrisk Woodfired Pizza restaurant</text>

  <!-- bottom strip phone, printed upside down -->
  <g class="bottom-phone" transform="rotate(180 300 528)">
    <path class="phone-icon" d="M230 518c-3 0-5 3-4 7 2 7 6 12 12 15 3 1 6-1 6-3l-4-4-3 2c-3-2-5-5-6-8l2-3z"/>
    <text class="script phone-text" x="252" y="535">(02) 5550-1847</text>
  </g>

  <!-- back wall -->
  <rect class="panel-beige" x="56" y="190" width="91" height="315"/>
  <g transform="translate(110 350) rotate(-90)">
    <rect class="brand-square-rust" x="-58" y="-14" width="14" height="14"/>
    <text class="script brand-dark" x="-38" y="0">lumbrisk</text>
  </g>

  <!-- base -->
  <rect class="panel-maroon" x="147" y="190" width="315" height="315"/>
  <circle cx="312" cy="330" r="108" fill="var(--maroon-soft)" role="img" aria-label="Faint line illustration of a sliced pizza with one slice pulled out"/>

  <!-- front spine -->
  <rect class="panel-beige" x="462" y="190" width="90" height="315"/>
  <g transform="translate(500 354) rotate(90)">
    <rect class="brand-square-rust" x="-58" y="-14" width="14" height="14"/>
    <text class="script brand-dark" x="-38" y="0">lumbrisk</text>
  </g>

  <!-- lid -->
  <rect class="panel-maroon" x="552" y="190" width="316" height="315"/>
  <rect class="tuck" x="868" y="190" width="34" height="315"/>

  <g class="lid" transform="translate(552 505) rotate(-90)">
    <!-- brand -->
    <rect class="brand-square-rust" x="16" y="24" width="20" height="20"/>
    <text class="script brand-light" x="44" y="44" style="font-size:28px">lumbrisk</text>

    <!-- headline -->
    <text class="script lid-text headline" x="68" y="146" text-anchor="middle">Woodfired</text>
    <text class="script lid-text headline" x="68" y="172" text-anchor="middle">Pizza</text>

    <!-- address -->
    <text class="script lid-text address" x="308" y="20" text-anchor="end">G07/12 Lakeview Pde,</text>
    <text class="script lid-text address" x="308" y="33" text-anchor="end">Marlow Heights NSW 2199,</text>
    <text class="script lid-text address" x="308" y="46" text-anchor="end">Australia</text>

    <!-- pizza artwork -->
    <circle cx="212" cy="150" r="70" fill="var(--rust)" stroke="var(--cream)" stroke-width="3" role="img" aria-label="Line illustration of a sliced pizza with a server lifting one slice"/>

    <!-- dividers -->
    <line class="lid-rule" x1="12" y1="238" x2="308" y2="238"/>
    <line class="lid-rule" x1="172" y1="238" x2="172" y2="312"/>

    <!-- order -->
    <text class="script lid-text order-label" x="16" y="266">Order Now:</text>
    <text class="script lid-text order-phone" x="16" y="294">(02) 5550-1847</text>

    <!-- connect -->
    <text class="script lid-text connect-title" x="184" y="256">Connect with Us</text>
    <circle class="social-dot" cx="188" cy="268" r="4"/>
    <text class="script lid-text connect-item" x="196" y="271">facebook.com/Lumbrisk</text>
    <circle class="social-dot" cx="188" cy="282" r="4"/>
    <text class="script lid-text connect-item" x="196" y="285">@lumbriskwoodfiredpizza</text>
    <circle class="social-dot" cx="188" cy="296" r="4"/>
    <text class="script lid-text connect-item" x="196" y="299">@LumbriskPizza</text>
  </g>
</svg>
</body>
</html>
```